Valmoré Fine Jewelry needs a print advertisment design

Objective
Design a high impact elegant and classy print advertisment for placement in brochures and magazines and create banners with. The intent will be for the Target Audience to want to visit the physical store to want to view the bridal ring collection and make purchases. The first use will be in a brochure handed out to brides-to-be at a wedding vendor exhibition.
Format & Size: Pdf, A4 size (potrait)
* not that the edges of the ad might get trimmed for the brochure.
Overall Look & Feel
The creative suggested should align with the logo - its subtle yet distinctive style. The colours used would be a good reference to the kind of contrast colours we would like used for the print ad as well. The print must stand out from other ads that will be placed in 12 page brochure. We will not have a booth at the event to meet with potential customers like some other vendors, so we will like to really jump out to our audience that catch a glimpse of our ad in the brochure and be inclined to find more about us or share us with other people.
Target Audience
- Woman in the age group of 20 - 50 yrs
- Literate, Outgoing, Social
- English speaking
Description of Business
We are a afforable, handcrafted, high end jewelry retail store targeted at woman. The store is located in Lagos, Nigeria in a high end mall. The store offers 18karat gold jewelry with gemstones and diamonds for women, men and children - engagement rings, wedding bands, bangles, chanderlier earrings, watches, necklaces, men bracelets, baby earrings and much more. We are mostly known for our bridal jewelry: engagement ring and wedding bands. Most of our pieces and designed by us and highly skilled Italian designers and handcrafted in Italy. We offer an uncluttered highly sophisticated environment for consumers to shop at leisure. We are opened everyday, which is a great plus because there are very few luxury jewelry stores in Nigeria and fewer that are opened everyday. We love what we do and think love rocks!
The store is bright and features gold tones everywhere excuding luxury.
We also carry the world renowed Italian brands,
a) Brascelli
b) Matteo Varni
c) Lusq and so on
Social Networking
-Prominent mention of the store's Pictogram and Friendspace site encouraging Consumers to 'Like' us on FS and follow us on PG @valmorefinejewelry
Store Address & Timings
The store address and business hours of operations must be prominently mentioned.
Address: Palmcrest Arcade Mall
2nd Floor, 58 Okonkwo Adeyemi Road
Victoria Island, Lagos
Nigeria
+234-17364081, +234-8032617749
Timings: Open Everyday
Mon-Sat: 10:00am to 6:30pm, Sun: 1:00pm to 6:30pm
Photographs
We are thinking to mostly focus on our diamond engagement rings in the advert and mention the other items we carry in-store. I have attached a bunch of images of pieces in the store that we could use for the advert. I also attached a Marlowe ad I came across and like, i like the rings popping, the clean lines, identification with the marlowe colour, the play on the "Love" word and the idea the love fairy tale most women dream of.
Logo Colors & Fonts
Attached is the logo we presently use. we would like to play on these colors.
Please consider an option to include a version with a promotion sale somewhere on the flyer. Easter Sale: 20% Off all In-store Engagement rings, Wedding bands and other selected jewelry.* Date: April 1st to April 30th, 2014 *Does not apply to past purchase.
Thanx!

```html
<!DOCTYPE html>
<html lang="en">
<head>
<meta charset="utf-8">
<title>Valmoré Fine Jewelry — Bridal Collection</title>
<link rel="stylesheet" href="https://fonts.googleapis.com/css2?family=Kurale&display=swap">
<style>
  :root {
    --brown-deep: #240e05;
    --brown-mid: #4f2c18;
    --brown-glow: #80593f;
    --teal: #14909f;
    --teal-dark: #0f7f8d;
    --gold: #d9a93a;
    --gold-light: #f3d27a;
    --ink-light: #f4f4f1;
  }
  * { margin: 0; padding: 0; box-sizing: border-box; }
  html, body { width: 847px; height: 1200px; overflow: hidden; background: var(--brown-deep); }
  .ad {
    position: relative;
    width: 847px;
    height: 1200px;
    overflow: hidden;
    font-family: "Kurale", Georgia, serif;
    color: var(--ink-light);
  }
  .hero {
    position: absolute;
    inset: 0 0 357px 0;
    background: radial-gradient(ellipse 75% 65% at 55% 45%, var(--brown-glow) 0%, var(--brown-mid) 45%, var(--brown-deep) 100%);
  }
  .ring-photo {
    position: absolute;
    left: 222px;
    top: 105px;
    width: 410px;
    height: 565px;
    border-radius: 48% 48% 44% 44%;
    background: radial-gradient(ellipse at 55% 30%, #f6f1e6 0%, #d8c59a 22%, var(--gold) 48%, #8a6420 75%, rgba(90,55,25,0) 100%);
    opacity: 0.9;
  }
  .info-band {
    position: absolute;
    left: 0; right: 0; bottom: 0;
    height: 357px;
    background: var(--teal);
  }
  .brand-badge {
    position: absolute;
    left: 335px;
    top: 757px;
    width: 176px;
    height: 176px;
    border-radius: 50%;
    background: var(--teal);
    display: flex;
    align-items: center;
    justify-content: center;
  }
  .brand-name {
    font-size: 30px;
    color: var(--gold-light);
  }
  .store-details {
    position: absolute;
    left: 0; right: 0;
    top: 948px;
    text-align: center;
    font-size: 26px;
    line-height: 36.5px;
  }
  .store-details sup { font-size: 15px; line-height: 0; }
  .social {
    position: absolute;
    left: 46px;
    right: 20px;
    top: 1128px;
    display: flex;
    gap: 14px;
    font-size: 18.5px;
  }
  .social-item { display: flex; align-items: center; gap: 8px; }
  .social-mark {
    width: 27px; height: 27px;
    border-radius: 4px;
    background: var(--ink-light);
    flex: none;
  }
</style>
</head>
<body>
<main class="ad">
  <section class="hero">
    <div class="ring-photo" role="img" aria-label="Photograph of a yellow gold engagement ring with a princess-cut diamond and pavé-set band"></div>
  </section>

  <section class="info-band">
  </section>

  <div class="brand-badge">
    <span class="brand-name">Valmoré</span>
  </div>

  <address class="store-details" style="font-style: normal;">
    <p>Palmcrest Arcade Mall,</p>
    <p>2<sup>nd</sup> Floor, 58 Okonkwo Adeyemi Road Victoria Island, Lagos, Nigeria</p>
    <p>+234-17364081, +234-8032617749</p>
    <p>Open Everyday Mon-Sat: 10:00am to 6:30pm, Sun: 1:00pm to 6:30pm</p>
  </address>

  <footer class="social">
    <div class="social-item"><span class="social-mark"></span><span>Like us on Friendspace: valmorefinejewelry</span></div>
    <div class="social-item"><span class="social-mark"></span><span>Follow us on Pictogram: valmorefinejewelry</span></div>
  </footer>
</main>
</body>
</html>
```